Tolliver Partners
Business Cards, Letterhead, Envelope and 3-4 basic Power Point Slides
Tolliver Partners -
Creative Brief
Please submit designs for: Business Cards, Letterhead, No. 10 Envelope and 3-4 Basic Power Point Slides Please see our web site for more information: TolliverPartners.com
Corporate and Investor Services
We have already completed our logo and its is available for downloading. Please do not make changes to the logo.

```html
<!DOCTYPE html>
<html lang="en">
<head>
<meta charset="utf-8">
<title>Tolliver Partners – Stationery and Slide Set</title>
<link rel="stylesheet" href="https://fonts.googleapis.com/css2?family=Roboto:wght@400;700;900&family=Archivo+Black&display=swap">
<style>
  :root{
    --green:#5fb336;
    --green-dark:#3f8f1f;
    --green-light:#cfe9bd;
    --blue:#1c8fd0;
    --blue-deep:#0d4f8f;
    --cyan:#2ab3e6;
    --ink:#1d1d1d;
    --grey:#777;
    --paper:#ffffff;
    --line:#c9c9c9;
  }
  *{box-sizing:border-box;margin:0;padding:0}
  html,body{width:1200px;height:600px;overflow:hidden;background:var(--paper)}
  body{position:relative;font-family:"Roboto",Arial,sans-serif;color:var(--ink)}
  .backdrop{position:absolute;inset:0}
  .sheet{position:absolute;background:var(--paper);border:1px solid var(--line);box-shadow:0 1px 3px rgba(0,0,0,.25);overflow:hidden}
  .brand{font-family:"Roboto",Arial,sans-serif;font-weight:700;color:var(--green);display:flex;align-items:center;gap:4px;white-space:nowrap}
  .brand .dot{width:.9em;height:.9em;border-radius:50%;background:var(--green)}
  .slide-num{position:absolute;font-size:11px;font-weight:700;color:var(--ink)}

  /* slides */
  .slide{width:232px;height:156px;top:8px}
  .slide-title{font-family:"Roboto",Arial,sans-serif;font-weight:700;color:var(--green);font-size:15px;text-align:center}
  .slide-sub{font-size:6px;color:var(--grey);text-align:center;margin-top:2px}
  .slide--cover{left:12px}
  .slide--cover .head{height:58px;padding:8px 8px 0;position:relative}
  .slide--cover .brand{position:absolute;left:8px;top:26px;font-size:11px}
  .slide--cover .photo{position:absolute;left:0;right:0;bottom:0;height:98px;background:linear-gradient(180deg,#1d7fc4 0%,#0b3f7c 55%,#2aa4e0 100%)}
  .bullets{list-style:none;font-size:5.5px;color:var(--ink)}
  .bullets li{margin-bottom:5px;display:flex;align-items:center;gap:4px}
  .bullets li::before{content:"";width:3px;height:3px;background:var(--blue)}
  .side-text{font-size:4.5px;line-height:1.5;color:var(--ink);font-weight:700}

  .slide--list{left:276px}
  .slide--list .side{position:absolute;left:0;top:0;bottom:8px;width:62px;padding:8px 6px}
  .slide--list .side .brand{font-size:9px;margin-bottom:36px}
  .slide--list .bar{position:absolute;left:62px;right:0;top:0;height:34px;background:linear-gradient(180deg,var(--blue) 0%,var(--blue-deep) 100%);padding-top:6px}
  .slide--list .bar .slide-title{color:#fff;font-size:12px}
  .slide--list .bar .slide-sub{color:#d8ecf8;margin-top:1px}
  .slide--list .bullets{position:absolute;left:72px;top:44px}
  .slide--list .foot{position:absolute;left:0;right:0;bottom:0;height:8px;background:var(--green)}

  .slide--photo{left:552px}
  .slide--photo .slide-title{margin-top:8px}
  .slide--photo .brand{position:absolute;left:8px;top:30px;font-size:10px}
  .slide--photo .side-text{position:absolute;left:8px;top:56px;width:54px}
  .slide--photo .bullets{position:absolute;left:72px;top:42px}
  .slide--photo .photo{position:absolute;right:0;bottom:0;width:118px;height:70px;background:linear-gradient(180deg,#ffffff 0%,#d9e9f3 50%,#9cc3dc 100%)}

  /* letterhead */
  .letterhead{left:869px;top:8px;width:306px;height:503px}
  .lh-head{height:46px;background:linear-gradient(90deg,#ffffff 0%,var(--green-light) 45%,var(--green) 100%);text-align:right;padding:10px 12px 0}
  .lh-company{font-family:"Archivo Black",Arial,sans-serif;font-size:12px;color:var(--ink)}
  .lh-contact{font-size:4.5px;color:var(--ink);margin-top:6px}
  .lh-mark{position:absolute;left:0;right:0;top:352px;text-align:center;font-family:"Roboto",Arial,sans-serif;font-weight:700;font-size:44px;color:#c8dfbd;line-height:1}
  .lh-mark-sub{position:absolute;left:0;right:0;top:402px;text-align:center;font-weight:700;font-size:12px;letter-spacing:4px;color:#c8dfbd}
  .lh-foot{position:absolute;left:0;right:0;bottom:0;height:22px;background:linear-gradient(90deg,#ffffff 0%,var(--green-light) 60%,var(--green) 100%);text-align:center;font-size:6px;font-weight:700;color:var(--ink);padding-top:11px}

  /* business card */
  .card{left:48px;top:283px;width:312px;height:172px}
  .card-head{height:38px;background:linear-gradient(90deg,#ffffff 0%,var(--green-light) 40%,var(--green) 100%);padding:10px 12px 0}
  .card-name{font-family:"Archivo Black",Arial,sans-serif;font-size:15px;color:var(--ink)}
  .card-contact{position:absolute;left:14px;top:56px;font-family:"Archivo Black",Arial,sans-serif;font-size:7.5px;line-height:1.45;color:var(--ink)}
  .card .brand{position:absolute;right:22px;top:82px;font-size:18px}
  .card-foot{position:absolute;left:0;right:0;bottom:0;height:22px;background:linear-gradient(90deg,#ffffff 0%,var(--green-light) 60%,var(--green) 100%);text-align:center;font-size:7px;font-weight:700;padding-top:8px}

  /* envelope */
  .envelope{left:408px;top:374px;width:384px;height:190px}
  .env-return{position:absolute;left:14px;top:12px;font-size:5px;line-height:1.5;color:var(--ink)}
  .env-to{position:absolute;left:156px;top:88px;font-size:5.5px;line-height:1.5;color:var(--ink)}
  .env-foot{position:absolute;left:0;right:0;bottom:0;height:18px;background:linear-gradient(90deg,#ffffff 0%,var(--green-light) 60%,var(--green) 100%);text-align:center;font-size:6px;font-weight:700;padding-top:7px}
</style>
</head>
<body>

<svg class="backdrop" width="1200" height="600" viewBox="0 0 1200 600" aria-hidden="true">
  <defs>
    <linearGradient id="sweep-blue" x1="0" y1="0" x2="1" y2="0">
      <stop offset="0" stop-color="#1c8fd0"/>
      <stop offset=".45" stop-color="#4fc0ec"/>
      <stop offset="1" stop-color="#ffffff" stop-opacity="0"/>
    </linearGradient>
    <linearGradient id="sweep-green" x1="0" y1="0" x2="1" y2="0">
      <stop offset="0" stop-color="#ffffff" stop-opacity="0"/>
      <stop offset="1" stop-color="#7cc44f"/>
    </linearGradient>
  </defs>
  <path d="M0 210 C300 160 560 170 900 250 L900 330 C600 300 300 330 0 470 Z" fill="url(#sweep-blue)"/>
  <path d="M700 600 C900 560 1060 520 1200 470 L1200 600 Z" fill="url(#sweep-green)"/>
</svg>

<!-- Slide 1: cover -->
<section class="sheet slide slide--cover">
  <div class="head">
    <div class="slide-title">Insert Title Here</div>
    <div class="slide-sub">Subtitle Here</div>
    <div class="brand"><span class="dot"></span>Tolliver</div>
  </div>
  <div class="photo" role="img" aria-label="Photo of business team silhouettes in front of a blue globe"></div>
</section>
<span class="slide-num" style="left:240px;top:178px">1</span>

<!-- Slide 2: list with header bar -->
<section class="sheet slide slide--list">
  <div class="side">
    <div class="brand"><span class="dot"></span>Tolliver</div>
    <p class="side-text">Key point summary text<br>goes in this area</p>
  </div>
  <div class="bar">
    <div class="slide-title">Insert Title Here</div>
    <div class="slide-sub">Subtitle Here</div>
  </div>
  <ul class="bullets">
    <li>Item 1 – 1/4 goes here</li>
    <li>Item 2 – 1/4 goes here</li>
    <li>Item 3 – 1/4 goes here</li>
    <li>Item 4 – 1/4 goes here</li>
    <li>Item 5 – 1/4 goes here</li>
  </ul>
  <div class="foot"></div>
</section>
<span class="slide-num" style="left:508px;top:178px">2</span>

<!-- Slide 3: list with photo -->
<section class="sheet slide slide--photo">
  <div class="slide-title">Insert Title Here</div>
  <div class="slide-sub">Subtitle Here</div>
  <div class="brand"><span class="dot"></span>Tolliver</div>
  <p class="side-text">Key point summary text<br>goes in this area</p>
  <ul class="bullets">
    <li>Item 1 – 1/4 goes here</li>
    <li>Item 2 – 1/4 goes here</li>
    <li>Item 3 – 1/4 goes here</li>
    <li>Item 4 – 1/4 goes here</li>
    <li>Item 5 – 1/4 goes here</li>
  </ul>
  <div class="photo" role="img" aria-label="Photo of standing business people silhouettes"></div>
</section>
<span class="slide-num" style="left:796px;top:178px">3</span>

<!-- Letterhead -->
<section class="sheet letterhead">
  <header class="lh-head">
    <div class="lh-company">Tolliver Partners, LLC</div>
    <div class="lh-contact">4120 Maple Ridge Drive • Westfield, IL 60999 • Phone: 555-014-2290 • Email: info@TolliverPartners.com</div>
  </header>
  <div class="lh-mark">Tolliver</div>
  <div class="lh-mark-sub">PARTNERS</div>
  <footer class="lh-foot">www.tolliverpartners.com</footer>
</section>

<!-- Business card -->
<section class="sheet card">
  <header class="card-head"><div class="card-name">Mrs. Dana R. Whitfield</div></header>
  <address class="card-contact" style="font-style:normal">
    Tolliver Partners, LLC<br>
    4120 Maple Ridge Drive<br>
    Westfield, IL 60999<br>
    Phone: 555-014-2290<br>
    Email: info@TolliverPartners.com
  </address>
  <div class="brand"><span class="dot"></span>Tolliver</div>
  <footer class="card-foot">www.tolliverpartners.com</footer>
</section>

<!-- No. 10 envelope -->
<section class="sheet envelope">
  <address class="env-return" style="font-style:normal">
    Tolliver Partners, LLC<br>
    4120 Maple Ridge Drive<br>
    Westfield, IL 60999
  </address>
  <address class="env-to" style="font-style:normal">
    Tolliver Partners, LLC<br>
    4120 Maple Ridge Drive<br>
    Westfield, IL 60999
  </address>
  <footer class="env-foot">www.tolliverpartners.com</footer>
</section>

</body>
</html>
```